Team email banner for internal communications

We need a team email banner/header that will be applied to all internal communications from our department to other functions. The graphic should be optimized for Outlook and be landscape in layout. We have 5 different silo within our team and will need so will either need have a blank space to denote each team or have change in colors/graphics to denote each team (see current headers attached to job description). We are looking for a banner that combines our team logo (attached) with our team name, Regional Talent & Coaching Unit. The theme should be L&D and pharmaceutical in nature.

Need extra days to review

The text in the banner should be Regional Talent & Coaching Unit with the team logo (attached).

```html
<!DOCTYPE html>
<html lang="en">
<head>
<meta charset="UTF-8">
<title>Regional Talent &amp; Coaching Unit – Email Banner</title>
<link href="https://fonts.googleapis.com/css2?family=Poppins:wght@800&family=Montserrat:wght@600&display=swap" rel="stylesheet">
<style>
  :root {
    --page-bg: #abdfec;
    --banner-bg: #f1faea;
    --banner-bg-soft: #e6f5dc;
    --ink: #0c0c0c;
    --accent-red: #dc2a1f;
    --band-dark: #3a8f6e;
    --band-light: #8cc63f;
    --rule: #9ccc55;
    --tagline: #2a9a70;
    --photo-deep: #5d86a8;
    --photo-mid: #9fc4de;
    --photo-light: #cfe7d2;
    --corner-tone: #c6e6a0;
    --divider: #777777;
  }
  * { margin: 0; padding: 0; box-sizing: border-box; }
  html, body { width: 1200px; height: 532px; overflow: hidden; }
  body { background: var(--page-bg); position: relative; font-family: "Poppins", sans-serif; }

  .banner {
    position: absolute; left: 93px; top: 97px; width: 1014px; height: 338px;
    background: linear-gradient(120deg, var(--banner-bg) 40%, var(--banner-bg-soft) 100%);
    box-shadow: 0 6px 18px rgba(40, 90, 110, 0.25);
    overflow: hidden;
  }
  .banner-art { position: absolute; inset: 0; }

  .brand-dot {
    position: absolute; left: 502px; top: 92px; width: 36px; height: 36px;
    border-radius: 50%; background: var(--accent-red);
  }
  .brand-initials {
    position: absolute; left: 459px; top: 139px; width: 122px; text-align: center;
    font-weight: 800; font-size: 46px; line-height: 1; color: var(--ink); letter-spacing: -1px;
  }
  .brand-divider {
    position: absolute; left: 593px; top: 85px; width: 1.5px; height: 92px; background: var(--divider);
  }
  .brand-name {
    position: absolute; left: 607px; top: 74px;
    font-weight: 800; font-size: 33px; line-height: 36px; color: var(--ink);
    text-transform: uppercase; letter-spacing: -1px; white-space: nowrap;
  }

  .divider-rule { position: absolute; left: 459px; top: 203px; width: 400px; height: 1px; background: var(--rule); }

  .tagline {
    position: absolute; left: 458px; top: 214px;
    font-family: "Montserrat", sans-serif; font-weight: 600; font-size: 30px;
    color: var(--tagline); letter-spacing: 0.2px; white-space: nowrap;
  }
</style>
</head>
<body>
  <section class="banner">
    <svg class="banner-art" width="1014" height="338" viewBox="0 0 1014 338" xmlns="http://www.w3.org/2000/svg">
      <defs>
        <linearGradient id="photoTone" x1="0" y1="0" x2="1" y2="1">
          <stop offset="0" stop-color="var(--photo-light)"/>
          <stop offset="0.45" stop-color="var(--photo-mid)"/>
          <stop offset="1" stop-color="var(--photo-deep)"/>
        </linearGradient>
        <radialGradient id="cornerTone" cx="1" cy="0.2" r="0.9">
          <stop offset="0" stop-color="var(--corner-tone)" stop-opacity="0.9"/>
          <stop offset="1" stop-color="var(--corner-tone)" stop-opacity="0"/>
        </radialGradient>
      </defs>

      <rect class="corner-illustration" role="img" aria-label="Soft green decorative illustration area"
            x="800" y="0" width="214" height="230" fill="url(#cornerTone)"/>

      <path class="band-light" d="M0 0 L316 0 C325 140 420 270 603 338 L0 338 Z" fill="var(--band-light)"/>
      <path class="band-dark" d="M0 0 L305 0 C312 140 400 270 580 338 L0 338 Z" fill="var(--band-dark)"/>
      <path class="photo" role="img" aria-label="Photo of a scientist in a blue glove holding a glass slide with a seedling, with lab glassware and digital overlays"
            d="M0 0 L289 0 C296 140 380 270 550 338 L0 338 Z" fill="url(#photoTone)"/>
    </svg>

    <span class="brand-dot"></span>
    <span class="brand-initials">RTCU</span>
    <span class="brand-divider"></span>
    <h1 class="brand-name">Regional<br>Talent &amp;<br>Coaching Unit</h1>

    <div class="divider-rule"></div>
    <p class="tagline">Operational &amp; Capabilities</p>
  </section>
</body>
</html>
```